Business Card Revision

Need to redesign my business cards for a new professional look. We are a courier company. You can go to www.qvroutefast.com to see what we do. The trucks have an old company name (Nimble) on them but that is the company we are just now
changing the name.

Target Market(s)

Potential clients. We service the automotive, plumbing, printing, air freight industries as well as many others.

Industry/Entity Type

Business

Contact Information for Business Card

QVrushline
20583 Palmer Fenwick Parkway
Cincinnati, Oh 45317

Howard T. Lassiter
President

howie@qvroutefast.com

Main: (513) 555-0147

```html
<!DOCTYPE html>
<html lang="en">
<head>
<meta charset="utf-8">
<title>QV Routefast Business Card</title>
<link rel="stylesheet" href="https://fonts.googleapis.com/css2?family=Archivo+Black&family=Arimo:wght@400&family=Oxygen:wght@400;700&display=swap">
<style>
  :root {
    --backdrop: #d9d4cc;
    --card-white: #ffffff;
    --band-black: #0a0a0a;
    --steel-light: #eef0f2;
    --steel-mid: #b9bcc1;
    --steel-dark: #8d9096;
    --logo-silver: #6e7277;
    --logo-silver-light: #c9ccd0;
    --ink: #111111;
    --leather-dark: #0d0d0d;
    --leather-mid: #262626;
  }
  * { margin: 0; padding: 0; box-sizing: border-box; }
  html, body { width: 1200px; height: 933px; overflow: hidden; }
  body { background: var(--backdrop); position: relative; font-family: "Arimo", Arial, sans-serif; }

  .card { position: absolute; left: 274px; width: 652px; height: 373px; overflow: hidden; box-shadow: 0 6px 18px rgba(0,0,0,0.25); }
  .card-front { top: 64px; background: var(--card-white); }
  .card-back { top: 494px; background: radial-gradient(ellipse at 45% 40%, var(--leather-mid), var(--leather-dark) 75%); }

  .front-bg { position: absolute; inset: 0; }

  .brand-name {
    position: absolute; left: 50px; top: 96px;
    font-family: "Archivo Black", Arial, sans-serif; font-size: 38px;
    color: var(--logo-silver); letter-spacing: 1px; line-height: 1;
  }
  .tagline {
    position: absolute; left: 64px; top: 198px;
    font-family: "Archivo Black", Arial, sans-serif; font-size: 15px;
    color: var(--ink); transform: rotate(-3.2deg); transform-origin: left center;
    white-space: nowrap;
  }

  .holder { position: absolute; right: 20px; top: 234px; text-align: right; font-family: "Oxygen", sans-serif; color: var(--ink); }
  .holder-name { font-size: 26px; font-weight: 400; line-height: 1.1; }
  .holder-title { font-size: 19px; line-height: 1.2; }

  .contact-list { position: absolute; left: 25px; top: 262px; list-style: none; }
  .contact-item { display: flex; align-items: center; height: 25.6px; font-size: 18px; color: var(--ink); }
  .contact-icon { width: 14px; height: 14px; margin-right: 16px; flex: none; }

  .back-brand {
    position: absolute; left: 0; right: 0; top: 158px; text-align: center;
    font-family: "Archivo Black", Arial, sans-serif; font-size: 50px;
    color: var(--logo-silver-light); letter-spacing: 2px; line-height: 1;
  }
</style>
</head>
<body>

<section class="card card-front" aria-label="Business card front">
  <svg class="front-bg" width="652" height="373" viewBox="0 0 652 373">
    <defs>
      <linearGradient id="steel" x1="0" y1="0" x2="1" y2="1">
        <stop offset="0" stop-color="var(--steel-mid)"/>
        <stop offset="0.35" stop-color="var(--steel-light)"/>
        <stop offset="0.7" stop-color="var(--steel-mid)"/>
        <stop offset="1" stop-color="var(--steel-dark)"/>
      </linearGradient>
    </defs>
    <polygon points="0,232 652,196 652,214 0,250" fill="var(--band-black)"/>
    <polygon points="0,250 652,214 652,373 0,373" fill="url(#steel)"/>
  </svg>

  <div class="brand-name">QV ROUTEFAST</div>
  <div class="tagline">24 HOUR * RAPID RESPONSE</div>

  <div class="holder">
    <div class="holder-name">Howard T. Lassiter</div>
    <div class="holder-title">President</div>
  </div>

  <ul class="contact-list">
    <li class="contact-item">
      <svg class="contact-icon" viewBox="0 0 14 14"><rect width="14" height="14" fill="var(--ink)"/><path d="M3 5 Q7 2 11 5 L10 6.5 L8.5 5.8 L8.5 5 Q7 4.5 5.5 5 L5.5 5.8 L4 6.5 Z M4 8 H10 V11 H4 Z" fill="#fff"/></svg>
      513-555-0147
    </li>
    <li class="contact-item">
      <svg class="contact-icon" viewBox="0 0 14 14"><rect width="14" height="14" fill="var(--ink)"/><rect x="3" y="4" width="8" height="6" fill="#fff"/><path d="M3 4 L7 7.5 L11 4" stroke="var(--ink)" stroke-width="1" fill="none"/></svg>
      howie@qvroutefast.com
    </li>
    <li class="contact-item">
      <svg class="contact-icon" viewBox="0 0 14 14"><rect width="14" height="14" fill="var(--ink)"/><circle cx="7" cy="7" r="4" fill="none" stroke="#fff" stroke-width="1.2"/><path d="M3 7 H11 M7 3 V11" stroke="#fff" stroke-width="0.9"/></svg>
      www.qvroutefast.com
    </li>
    <li class="contact-item">
      <svg class="contact-icon" viewBox="0 0 14 14"><rect width="14" height="14" fill="var(--ink)"/><path d="M7 11.5 L4.5 7 A2.8 2.8 0 1 1 9.5 7 Z" fill="#fff"/><circle cx="7" cy="5.8" r="1" fill="var(--ink)"/></svg>
      20583 Palmer Fenwick Parkway, Cincinnati, Oh 45317
    </li>
  </ul>
</section>

<section class="card card-back" aria-label="Business card back">
  <div class="back-brand">QV ROUTEFAST</div>
</section>

</body>
</html>
```